Tidal Pastry Depot Business card

We are empanada whole-sellers and I want a business card design with a picture of an empanada on it that also mentions first trial order FREE. our contact number 555-274-1193 our website www.zarifaban.com and business email Tomas@zarifaban.com

If you want any of our artwork please feel free to email me at the address above.

```html
<!DOCTYPE html>
<html lang="en">
<head>
<meta charset="utf-8">
<title>Tidal Pastry Depot Business Card</title>
<link href="https://fonts.googleapis.com/css2?family=Merriweather:wght@700;900&display=swap" rel="stylesheet">
<style>
  :root {
    --page: #ffffff;
    --ink: #1f1d1b;
    --offer-bg: #e5e5e4;
    --gold: #e8b727;
    --gold-deep: #d9a61c;
    --pastry-light: #f6c46a;
    --pastry-dark: #d98e2c;
    --shadow: rgba(0, 0, 0, 0.18);
  }
  html, body {
    margin: 0;
    padding: 0;
    width: 1200px;
    height: 921px;
    overflow: hidden;
    background: var(--page);
  }
  .canvas {
    position: relative;
    width: 1200px;
    height: 921px;
    font-family: "Merriweather", Georgia, serif;
    color: var(--ink);
  }
  .card {
    position: absolute;
    box-sizing: border-box;
    box-shadow: 4px 6px 8px var(--shadow);
  }

  /* Offer side */
  .card-offer {
    left: 153px;
    top: 163px;
    width: 568px;
    height: 326px;
    background: var(--offer-bg);
    border: 6px solid var(--gold);
  }
  .offer-headline {
    position: absolute;
    left: 42px;
    top: 34px;
    margin: 0;
    font-weight: 900;
    line-height: 1;
  }
  .offer-first { display: block; font-size: 44px; }
  .offer-trial { display: block; font-size: 27px; margin: 6px 0 0 48px; font-weight: 700; }
  .offer-free  { display: block; font-size: 62px; margin: 4px 0 0 22px; }
  .pastry-art {
    position: absolute;
    left: 352px;
    top: 44px;
    width: 180px;
    height: 106px;
    border-radius: 60px 60px 40px 40px;
    background: radial-gradient(ellipse at 45% 35%, var(--pastry-light), var(--pastry-dark));
  }
  .divider {
    position: absolute;
    left: 42px;
    top: 193px;
    width: 490px;
    height: 0;
    border-top: 3px solid var(--ink);
  }
  .contact {
    position: absolute;
    left: 42px;
    top: 218px;
    margin: 0;
    font-style: normal;
    font-weight: 700;
    font-size: 16px;
    line-height: 22px;
  }

  /* Brand side */
  .card-brand {
    left: 443px;
    top: 396px;
    width: 582px;
    height: 330px;
    background: var(--gold);
    border: 6px solid var(--ink);
    text-align: center;
  }
  .corner-mark {
    position: absolute;
    width: 40px;
    height: 40px;
    border-radius: 50%;
    background: var(--ink);
  }
  .corner-mark.top-left { left: 34px; top: 26px; }
  .corner-mark.bottom-right { right: 34px; bottom: 36px; }
  .brand-name {
    position: absolute;
    left: 0;
    right: 0;
    top: 106px;
    margin: 0;
    font-size: 40px;
    font-weight: 900;
    color: var(--ink);
  }
  .brand-tagline {
    position: absolute;
    left: 0;
    right: 0;
    top: 176px;
    margin: 0;
    font-size: 14px;
    font-weight: 900;
    line-height: 20px;
    letter-spacing: 0.5px;
  }
</style>
</head>
<body>
<main class="canvas">
  <section class="card card-offer">
    <h1 class="offer-headline">
      <span class="offer-first">FIRST</span>
      <span class="offer-trial">TRIAL ORDER</span>
      <span class="offer-free">FREE</span>
    </h1>
    <div class="pastry-art" role="img" aria-label="Illustration of three golden baked empanadas"></div>
    <div class="divider"></div>
    <address class="contact">
      555-274-1193<br>
      Tomas@zarifaban.com<br>
      www.zarifaban.com
    </address>
  </section>

  <section class="card card-brand">
    <div class="corner-mark top-left" role="img" aria-label="Small black flower ornament"></div>
    <h2 class="brand-name">Tidal Pastry Depot</h2>
    <p class="brand-tagline">WHOLESALE<br>CURRY PUFFS &amp; EMPANADAS</p>
    <div class="corner-mark bottom-right" role="img" aria-label="Small black flower ornament"></div>
  </section>
</main>
</body>
</html>
```